Rosa Caring Star registered NDIS provider

Quality Care, Endless Support: Your NDIS Journey Starts Here
Rosa Caring Star is a compassionate Disability Support Service based in Liverpool NSW . We will provide you and your loved ones professional care and support that is tailored to your individual needs. We offer approved specialised short to long term disability accommodations, support independent living (SIL), assistance with daily tasks including cleaning, meal preparation and gardening, as well as daily programs and activities that range from personal training, community outings, videogames, table tennis, arts and craft, movies, and so much more!
To learn more about our services, feel free to browse our website to read about our NDIS-related blogs. For more information, get in touch with our friendly staff.
Work with Rosa Caring Star today. You and your loved ones deserve only the best.

Rosa Caring Star
registered NDIS provider
Our services:
Approved specialised disability accommodations.

Support independent living SIL.

Short term accommodations/tenancy & respite.

Development of daily living & life skills

Overnight care active/non-active

Group/day centre activities

Assist in personal care.

Participation in community

Social and civic activities

Daily personal activities

Household tasks

Lawn mowing

Lifelong learning

Daily activities

Meal preparations

Support coordination

Plan management

Registered NDIS Provider
address 47 Brindle Crescent Wattlebrook NSW 2999
Phone : 0293416578/0471593824
Email : info@rosacaring.example.com.au
Web: : www.rosacaring.example.com.au
our servises in arabic
الخدمات تشمل
١- مساعدة التنقل .

٢- المشاركة الاجتماعية .

٣- تنمية المهارات الحياتية .

٤- مساعدة الأنشطة الشخصية .

٥- المساعدة في المهام المنزلية .

٦- مبيت (Respite ) وعناية على مدار ٢٤ ساعة .

٧- تطوير كافة المهارات اليومية مثلا تعلم الطبخ والميكاب تطوير المهارات الاجتماعية والحياة اليومية و طرق التنقل الامن مثل الباص و القطار
٨- العناية الشخصية والجسدية .
بإلاضافة الى السفرات الفردية والجماعية لمختلف الاعمار .

٩- بيوت مجهزة للسكن الدائمي لخدمات ذوي الاحتياجات الخاصه مع رعايه على مدار ٢٤ ساعة .

Target Market(s)

Disabilty people they need services from ndis provider which is my company registered company with ndis

Industry/Entity Type

Ndis disability services

Font styles to use
Serif

Colors
59FF00
82FF00
B8FF75
E3FFCB
F4FFEA
A7469A
B969AE
D3A5CF
EDDBEB
F8F0F9

Requirements
Must have
• Ndis logo and nice pictures for peoples with disability age from 9 years to 65 years
Should not have
• Old people

```html
<!DOCTYPE html>
<html lang="en">
<head>
<meta charset="utf-8">
<title>Rosa Caring Star – Our Services</title>
<link rel="stylesheet" href="https://fonts.googleapis.com/css2?family=Montserrat:wght@400;500;600;700&display=swap">
<style>
  :root {
    --backdrop: #cfcfcf;
    --paper: #ffffff;
    --leaf-green: #76bf43;
    --plum: #7c2a7e;
    --ink: #1d1d1b;
    --white: #ffffff;
  }
  html, body {
    margin: 0;
    padding: 0;
    width: 1200px;
    height: 1200px;
    overflow: hidden;
    background: var(--backdrop);
    font-family: "Montserrat", Arial, sans-serif;
  }
  .flyer {
    position: absolute;
    left: 230px;
    top: 77px;
    width: 740px;
    height: 1046px;
    background: var(--paper);
    overflow: hidden;
  }
  .flyer-shapes {
    position: absolute;
    inset: 0;
    width: 740px;
    height: 1046px;
  }
  .services-title {
    position: absolute;
    left: 45px;
    top: 42px;
    margin: 0;
    font-size: 45px;
    font-weight: 700;
    color: var(--white);
    letter-spacing: 0.3px;
  }
  .services-list {
    position: absolute;
    left: 45px;
    top: 129px;
    margin: 0;
    padding: 0;
    list-style: none;
  }
  .services-list li {
    display: flex;
    align-items: center;
    height: 25px;
    font-size: 15.5px;
    font-weight: 400;
    color: var(--white);
  }
  .services-list .tick {
    width: 14px;
    height: 14px;
    margin-right: 13px;
    flex: none;
  }
  .contact {
    position: absolute;
    right: 48px;
    top: 600px;
    text-align: right;
    color: var(--ink);
  }
  .contact-heading {
    margin: 0 18px 16px 0;
    font-size: 16.5px;
    font-weight: 700;
    letter-spacing: 0.2px;
  }
  .contact-row {
    display: flex;
    justify-content: flex-end;
    align-items: flex-start;
    font-size: 14.5px;
    font-weight: 500;
    line-height: 18px;
  }
  .contact-row .icon {
    width: 10px;
    height: 10px;
    margin: 4px 0 0 8px;
    flex: none;
  }
  .contact-address { margin-bottom: 16px; }
  .brand {
    position: absolute;
    left: 80px;
    top: 915px;
    display: flex;
    align-items: center;
    gap: 18px;
  }
  .brand-dot {
    width: 40px;
    height: 40px;
    border-radius: 50%;
    background: var(--leaf-green);
    flex: none;
  }
  .brand-name {
    margin: 0;
    font-size: 30px;
    font-weight: 500;
    line-height: 40px;
    color: var(--ink);
    white-space: nowrap;
  }
</style>
</head>
<body>
  <main class="flyer">
    <svg class="flyer-shapes" viewBox="0 0 740 1046" aria-hidden="true">
      <path class="green-field" fill="var(--leaf-green)"
            d="M0,0 H740 V348 C600,392 480,470 400,560 C340,628 160,648 0,560 Z"/>
      <path class="plum-swoosh" fill="var(--plum)"
            d="M740,356 C560,420 330,480 305,620 C290,720 420,790 551,804 C440,770 360,710 372,625 C385,520 560,430 740,356 Z"/>
    </svg>

    <h1 class="services-title">Our Services:</h1>
    <ul class="services-list">
      <li><svg class="tick" viewBox="0 0 14 14"><path d="M2 7.5 L5.5 11 L12 3" fill="none" stroke="#fff" stroke-width="2.2" stroke-linecap="round" stroke-linejoin="round"/></svg>Approved specialised disability accommodations.</li>
      <li><svg class="tick" viewBox="0 0 14 14"><path d="M2 7.5 L5.5 11 L12 3" fill="none" stroke="#fff" stroke-width="2.2" stroke-linecap="round" stroke-linejoin="round"/></svg>Support independent living SIL.</li>
      <li><svg class="tick" viewBox="0 0 14 14"><path d="M2 7.5 L5.5 11 L12 3" fill="none" stroke="#fff" stroke-width="2.2" stroke-linecap="round" stroke-linejoin="round"/></svg>Short term accommodations/tenancy &amp; respite.</li>
      <li><svg class="tick" viewBox="0 0 14 14"><path d="M2 7.5 L5.5 11 L12 3" fill="none" stroke="#fff" stroke-width="2.2" stroke-linecap="round" stroke-linejoin="round"/></svg>Development of daily living &amp; life skills</li>
      <li><svg class="tick" viewBox="0 0 14 14"><path d="M2 7.5 L5.5 11 L12 3" fill="none" stroke="#fff" stroke-width="2.2" stroke-linecap="round" stroke-linejoin="round"/></svg>Overnight care active/non-active</li>
      <li><svg class="tick" viewBox="0 0 14 14"><path d="M2 7.5 L5.5 11 L12 3" fill="none" stroke="#fff" stroke-width="2.2" stroke-linecap="round" stroke-linejoin="round"/></svg>Group/day centre activities</li>
      <li><svg class="tick" viewBox="0 0 14 14"><path d="M2 7.5 L5.5 11 L12 3" fill="none" stroke="#fff" stroke-width="2.2" stroke-linecap="round" stroke-linejoin="round"/></svg>Assist in personal care.</li>
      <li><svg class="tick" viewBox="0 0 14 14"><path d="M2 7.5 L5.5 11 L12 3" fill="none" stroke="#fff" stroke-width="2.2" stroke-linecap="round" stroke-linejoin="round"/></svg>Participation in community</li>
      <li><svg class="tick" viewBox="0 0 14 14"><path d="M2 7.5 L5.5 11 L12 3" fill="none" stroke="#fff" stroke-width="2.2" stroke-linecap="round" stroke-linejoin="round"/></svg>Social and civic activities</li>
      <li><svg class="tick" viewBox="0 0 14 14"><path d="M2 7.5 L5.5 11 L12 3" fill="none" stroke="#fff" stroke-width="2.2" stroke-linecap="round" stroke-linejoin="round"/></svg>Daily personal activities</li>
      <li><svg class="tick" viewBox="0 0 14 14"><path d="M2 7.5 L5.5 11 L12 3" fill="none" stroke="#fff" stroke-width="2.2" stroke-linecap="round" stroke-linejoin="round"/></svg>Household tasks</li>
      <li><svg class="tick" viewBox="0 0 14 14"><path d="M2 7.5 L5.5 11 L12 3" fill="none" stroke="#fff" stroke-width="2.2" stroke-linecap="round" stroke-linejoin="round"/></svg>Lawn mowing</li>
      <li><svg class="tick" viewBox="0 0 14 14"><path d="M2 7.5 L5.5 11 L12 3" fill="none" stroke="#fff" stroke-width="2.2" stroke-linecap="round" stroke-linejoin="round"/></svg>Lifelong learning</li>
      <li><svg class="tick" viewBox="0 0 14 14"><path d="M2 7.5 L5.5 11 L12 3" fill="none" stroke="#fff" stroke-width="2.2" stroke-linecap="round" stroke-linejoin="round"/></svg>Daily activities</li>
      <li><svg class="tick" viewBox="0 0 14 14"><path d="M2 7.5 L5.5 11 L12 3" fill="none" stroke="#fff" stroke-width="2.2" stroke-linecap="round" stroke-linejoin="round"/></svg>Meal preparations</li>
      <li><svg class="tick" viewBox="0 0 14 14"><path d="M2 7.5 L5.5 11 L12 3" fill="none" stroke="#fff" stroke-width="2.2" stroke-linecap="round" stroke-linejoin="round"/></svg>Support coordination</li>
      <li><svg class="tick" viewBox="0 0 14 14"><path d="M2 7.5 L5.5 11 L12 3" fill="none" stroke="#fff" stroke-width="2.2" stroke-linecap="round" stroke-linejoin="round"/></svg>Plan management</li>
    </ul>

    <section class="contact">
      <h2 class="contact-heading">REGISTERED NDIS PROVIDER</h2>
      <div class="contact-row contact-address">
        <span>47 Brindle Crescent<br>Wattlebrook NSW 2999</span>
        <svg class="icon" viewBox="0 0 10 10"><path d="M5 0.5 C2.8 0.5 1.5 2 1.5 3.8 C1.5 6 5 9.5 5 9.5 C5 9.5 8.5 6 8.5 3.8 C8.5 2 7.2 0.5 5 0.5 Z" fill="var(--ink)"/><circle cx="5" cy="3.8" r="1.3" fill="#fff"/></svg>
      </div>
      <div class="contact-row">
        <span>0293416578 / 0471593824</span>
        <svg class="icon" viewBox="0 0 10 10"><path d="M2 0.8 L3.8 0.8 L4.5 3 L3.3 4 C3.9 5.3 4.7 6.1 6 6.7 L7 5.5 L9.2 6.2 L9.2 8 C9.2 8.8 8.6 9.3 7.8 9.2 C4.2 8.8 1.2 5.8 0.8 2.2 C0.7 1.4 1.2 0.8 2 0.8 Z" fill="var(--ink)"/></svg>
      </div>
      <div class="contact-row">
        <span>info@rosacaring.example.com.au</span>
        <svg class="icon" viewBox="0 0 10 10"><rect x="0.5" y="2" width="9" height="6.5" rx="0.8" fill="var(--ink)"/><path d="M0.8 2.4 L5 5.6 L9.2 2.4" fill="none" stroke="#fff" stroke-width="0.8"/></svg>
      </div>
      <div class="contact-row">
        <span>www.rosacaring.example.com.au</span>
        <svg class="icon" viewBox="0 0 10 10"><circle cx="5" cy="5" r="4.3" fill="none" stroke="var(--ink)" stroke-width="1.2"/><path d="M0.8 5 H9.2 M5 0.8 C3 3 3 7 5 9.2 M5 0.8 C7 3 7 7 5 9.2" fill="none" stroke="var(--ink)" stroke-width="0.9"/></svg>
      </div>
    </section>

    <div class="brand">
      <span class="brand-dot"></span>
      <p class="brand-name">Rosa Caring Star</p>
    </div>
  </main>
</body>
</html>
```